Voltline Assemblies, Inc. Business Card

Voltline has three operating entities and I'm looking for a standard business card template that can be used for Voltline and the three operating entities that the logo just get swapped out, but has a very similar look and feel. Ultimately if someone had a business card from each, they assume the organizations are related because they all have the same look and feel.
Below are our websites and I will attached the logos for each entity:
https://www.voltlineassemblies.example/
https://www.brantoceramic.example/
https://www.omra-kfsd.example/
https://www.summitbreaker.example/

Target Market(s)

US Voltline

Industry/Entity Type

US Voltline

Contact Information for Business Card

Normal stuff

```html
<!DOCTYPE html>
<html lang="en">
<head>
<meta charset="utf-8">
<title>Voltline Assemblies, Inc. Business Card</title>
<link rel="stylesheet" href="https://fonts.googleapis.com/css2?family=Montserrat:wght@500;600;800&family=Roboto:wght@400;500&display=swap">
<style>
  :root {
    --navy: #2b3a78;
    --navy-light: #43548f;
    --red: #d2344a;
    --white: #ffffff;
    --ink: #555b66;
    --stage: #2a2a2c;
  }
  * { box-sizing: border-box; margin: 0; padding: 0; }
  html, body { width: 1200px; height: 929px; overflow: hidden; background: var(--stage); }
  .canvas { position: relative; width: 1200px; height: 929px; }

  .card {
    position: absolute;
    width: 600px; height: 343px;
    border-radius: 16px;
    overflow: hidden;
    box-shadow: 0 18px 40px rgba(0,0,0,.45);
  }

  /* Front */
  .card-front { left: 70px; top: 80px; background: linear-gradient(135deg, var(--navy) 0%, var(--navy-light) 100%); }
  .front-logo { position: absolute; left: 0; right: 0; top: 58px; display: flex; flex-direction: column; align-items: center; }
  .brand-mark { width: 64px; height: 64px; border-radius: 50%; margin-bottom: 10px; }
  .card-front .brand-mark { background: var(--white); }
  .brand-name { font-family: 'Montserrat', sans-serif; font-weight: 800; font-size: 44px; letter-spacing: 1px; line-height: 1; }
  .brand-sub { font-family: 'Montserrat', sans-serif; font-weight: 500; font-size: 15px; letter-spacing: 5px; color: var(--red); margin-top: 6px; }
  .card-front .brand-name { color: var(--white); }

  .entity-band {
    position: absolute; left: 0; right: 0; top: 250px; height: 68px;
    background: var(--white);
    display: flex; justify-content: space-around; align-items: center;
    padding: 0 16px;
  }
  .entity { display: flex; align-items: center; gap: 7px; }
  .entity-square { width: 18px; height: 18px; background: var(--navy); flex: none; }
  .entity-text { display: flex; flex-direction: column; }
  .entity-name { font-family: 'Montserrat', sans-serif; font-weight: 600; font-size: 11px; color: var(--navy); line-height: 1.2; }
  .entity-note { font-family: 'Roboto', sans-serif; font-size: 6px; color: var(--ink); margin-top: 2px; }
  .front-foot { position: absolute; left: 0; right: 0; bottom: 0; height: 25px; background: var(--navy); }

  /* Back */
  .card-back { left: 530px; top: 506px; background: var(--white); }
  .back-logo { position: absolute; left: 34px; top: 62px; width: 230px; display: flex; flex-direction: column; align-items: center; }
  .card-back .brand-mark { background: var(--navy); }
  .card-back .brand-name { color: var(--navy); font-size: 38px; }
  .card-back .brand-sub { font-size: 13px; letter-spacing: 4px; }

  .divider { position: absolute; left: 286px; top: 44px; width: 1px; height: 160px; background: var(--navy); }
  .contact { position: absolute; left: 306px; top: 46px; }
  .person-name { font-family: 'Montserrat', sans-serif; font-weight: 800; font-size: 19px; color: var(--navy); letter-spacing: .5px; }
  .person-title { font-family: 'Roboto', sans-serif; font-size: 14px; color: var(--red); margin-top: 2px; }
  .address { font-family: 'Roboto', sans-serif; font-size: 12px; color: var(--ink); margin-top: 18px; line-height: 1.35; }
  .contact-list { list-style: none; margin-top: 10px; }
  .contact-list li { display: flex; align-items: center; gap: 8px; font-family: 'Roboto', sans-serif; font-size: 12px; color: var(--ink); line-height: 1.6; }
  .contact-list svg { width: 12px; height: 12px; flex: none; }

  .web-band { position: absolute; left: 0; right: 0; top: 256px; height: 44px; background: var(--navy); display: flex; align-items: center; padding-left: 120px; }
  .web-band span { font-family: 'Roboto', sans-serif; font-weight: 400; font-size: 15px; letter-spacing: 2px; color: var(--white); }
  .red-tab { position: absolute; right: 0; top: 218px; width: 112px; height: 38px; background: var(--red); }
  .band-mark { position: absolute; right: 76px; top: 226px; width: 58px; height: 58px; border-radius: 50%; background: var(--white); border: 4px solid var(--navy); }
  .back-foot { position: absolute; left: 0; right: 0; bottom: 0; height: 34px; background: var(--navy); }
</style>
</head>
<body>
<div class="canvas">

  <section class="card card-front" aria-label="Card front">
    <div class="front-logo">
      <div class="brand-mark"></div>
      <div class="brand-name">VOLTLINE</div>
      <div class="brand-sub">ASSEMBLIES, INC.</div>
    </div>
    <div class="entity-band">
      <div class="entity">
        <div class="entity-square"></div>
        <div class="entity-text">
          <span class="entity-name">Omra Instrument Corporation</span>
          <span class="entity-note">A Voltline Assemblies, Inc. Company</span>
        </div>
      </div>
      <div class="entity">
        <div class="entity-square"></div>
        <div class="entity-text">
          <span class="entity-name">Branto Ceramic, LLC</span>
          <span class="entity-note">A Voltline Assemblies, Inc. Company</span>
        </div>
      </div>
      <div class="entity">
        <div class="entity-square"></div>
        <div class="entity-text">
          <span class="entity-name">Summit Breaker</span>
          <span class="entity-note">A Voltline Assemblies, Inc. Company</span>
        </div>
      </div>
    </div>
    <div class="front-foot"></div>
  </section>

  <section class="card card-back" aria-label="Card back">
    <div class="back-logo">
      <div class="brand-mark"></div>
      <div class="brand-name">VOLTLINE</div>
      <div class="brand-sub">ASSEMBLIES, INC.</div>
    </div>
    <div class="divider"></div>
    <div class="contact">
      <div class="person-name">MARCUS ELLERY</div>
      <div class="person-title">Founder &amp; CEO</div>
      <div class="address">48 Harrow Bend Road,<br>Lakeview, ON K2P 0R4</div>
      <ul class="contact-list">
        <li>
          <svg viewBox="0 0 12 12"><path fill="#d2344a" d="M1 4c0-2 2-3 5-3s5 1 5 3l-2 1-1-2H4L3 5 1 4zm2 2h6l1 5H2l1-5zm3 1a1.5 1.5 0 1 0 0 3 1.5 1.5 0 0 0 0-3z"/></svg>
          555.014.2210
        </li>
        <li>
          <svg viewBox="0 0 12 12"><rect x="3" y="0.5" width="6" height="11" rx="1" fill="none" stroke="#d2344a" stroke-width="1.2"/><rect x="5" y="9" width="2" height="1" fill="#d2344a"/></svg>
          555.019.7734
        </li>
        <li>
          <svg viewBox="0 0 12 12"><rect x="0.5" y="2" width="11" height="8" fill="#d2344a"/><path d="M0.5 2L6 7l5.5-5" fill="none" stroke="#fff" stroke-width="1"/></svg>
          info@voltlineassemblies.example
        </li>
      </ul>
    </div>
    <div class="red-tab"></div>
    <div class="web-band"><span>www.voltlineassemblies.example</span></div>
    <div class="band-mark"></div>
    <div class="back-foot"></div>
  </section>

</div>
</body>
</html>
```